Delwyn's Pressure Washing Services

Starting a pressure washing business on my own in Central Valley California, not too much experience so affordable, I do houses, fences, driveways, cars, trailers, RVs. Planning to make this full-time hoping clientele picks up after having a nice business card. Design doesn't have to be flashy, more to the point, I like simplistic/personable. I do not want something exhausting to look at or with too much going on.

Target Market(s)

Residential, Commercial

Industry/Entity Type

Pressure Washing

Contact Information for Business Card

avalible Services

Font styles to use
Sans Serif

Colors
0054AA
0677BA
7BADD7
CADEEF
E8F1F8
0094D4
00A9DD
6FCCEA
C7EBF8
E9F6FB
00AB8E
00BBA5
67D7C9
C6EFE9
E9F9F6

```html
<!DOCTYPE html>
<html lang="en">
<head>
<meta charset="utf-8">
<title>Delwyn's Pressure Washing Services – Business Card</title>
<link rel="stylesheet" href="https://fonts.googleapis.com/css2?family=Poppins:wght@400;500;600;700&display=swap">
<style>
  :root {
    --page-bg: #dfe4e9;
    --card-top: #eef3f7;
    --card-bottom: #e3eaf0;
    --brand-deep: #0054AA;
    --brand-mid: #0677BA;
    --brand-sky: #0094D4;
    --brand-light: #6FCCEA;
    --ink-dark: #1b3a5c;
    --ink-body: #22507e;
  }
  html, body {
    margin: 0;
    width: 1200px;
    height: 970px;
    overflow: hidden;
    background: var(--page-bg);
    font-family: "Poppins", sans-serif;
  }
  .stage {
    width: 1200px;
    height: 970px;
    display: flex;
    align-items: center;
    justify-content: center;
  }
  .business-card {
    width: 1100px;
    height: 628px;
    box-shadow: 0 18px 40px rgba(20, 50, 80, 0.18);
    display: block;
  }
  .brand-name { font-family: "Poppins", sans-serif; font-weight: 600; fill: var(--brand-mid); }
  .brand-tagline { font-family: "Poppins", sans-serif; font-weight: 600; fill: var(--brand-mid); letter-spacing: 5px; }
  .owner-name { font-family: "Poppins", sans-serif; font-weight: 700; fill: var(--ink-dark); }
  .contact-line, .services-line { font-family: "Poppins", sans-serif; font-weight: 400; fill: var(--ink-body); }
</style>
</head>
<body>
<main class="stage">
  <svg class="business-card" viewBox="0 0 1040 594" xmlns="http://www.w3.org/2000/svg" aria-label="Delwyn's Pressure Washing Services business card">
    <defs>
      <linearGradient id="cardFace" x1="0" y1="0" x2="0" y2="1">
        <stop offset="0" stop-color="var(--card-top)"/>
        <stop offset="1" stop-color="var(--card-bottom)"/>
      </linearGradient>
      <linearGradient id="splashTone" x1="0" y1="0" x2="1" y2="1">
        <stop offset="0" stop-color="#2f9bd0"/>
        <stop offset="1" stop-color="#0a72b4"/>
      </linearGradient>
      <linearGradient id="bubbleTone" x1="0" y1="0" x2="1" y2="1">
        <stop offset="0" stop-color="#1f8fc8"/>
        <stop offset="1" stop-color="#6bbcdc"/>
      </linearGradient>
    </defs>

    <rect class="card-face" width="1040" height="594" fill="url(#cardFace)"/>

    <path class="decor-bubbles" role="img" aria-label="Decorative water bubbles"
          d="M0 0 H230 C230 110 170 190 0 200 Z" fill="url(#bubbleTone)" opacity="0.85"/>

    <path class="decor-splash" role="img" aria-label="Decorative water splash"
          d="M320 0 H1040 V112 C900 60 760 120 600 150 C470 170 330 130 320 0 Z" fill="url(#splashTone)"/>

    <path class="decor-corner" d="M800 594 C890 570 985 520 1040 455 V594 Z" fill="#1e8cc8"/>

    <g class="brand-block">
      <text class="brand-name" x="408" y="310" font-size="86">Delwyn's</text>
      <text class="brand-tagline" x="424" y="366" font-size="16">PRESSURE WASHING SERVICES</text>
    </g>

    <g class="contact-block">
      <text class="owner-name" x="56" y="404" font-size="30">DELWYN MARSH</text>

      <path class="icon-phone" d="M63 434 c-3 0 -4 3 -4 6 c0 6 5 12 11 13 c3 0 5 -1 5 -3 l-3 -3 l-3 1 c-2 -1 -4 -4 -4 -6 l1 -3 z" fill="var(--ink-dark)"/>
      <text class="contact-line" x="88" y="456" font-size="26">2095550147</text>

      <g class="icon-mail">
        <rect x="58" y="473" width="17" height="12" fill="var(--ink-dark)"/>
        <path d="M58 473 L66.5 480 L75 473" fill="none" stroke="var(--card-top)" stroke-width="1.5"/>
      </g>
      <text class="contact-line" x="88" y="487" font-size="26">hello@delwynwash.com</text>

      <text class="services-line" x="56" y="538" font-size="25">Houses | Fences | Driveways | Cars | Trailers | RVs clening</text>
    </g>
  </svg>
</main>
</body>
</html>
```